Business Card Project

We are a small consulting firm. You can experiment with any design.
Must have:
1) Company name - OLUNDEX International
2) Company slogan - simple solutions for complex problems
3) Name/Title/Phone/Email/WWW/ - use anything you like as an example.

Industry/Entity Type

Business

```html
<!DOCTYPE html>
<html lang="en">
<head>
<meta charset="utf-8">
<title>OLUNDEX International – Business Card</title>
<link rel="stylesheet" href="https://fonts.googleapis.com/css2?family=Crimson+Text:wght@400;700&family=Shadows+Into+Light&display=swap">
<style>
  :root {
    --card-white: #ffffff;
    --brand-navy: #002187;
    --brand-gold: #d9b100;
    --ink: #000000;
    --page-bg: #ffffff;
  }
  html, body {
    margin: 0;
    padding: 0;
    width: 1200px;
    height: 686px;
    overflow: hidden;
    background: var(--page-bg);
  }
  .business-card {
    display: block;
    width: 1200px;
    height: 686px;
  }
  .card-base { fill: var(--card-white); }
  .wave-gold { fill: var(--brand-gold); }
  .wave-navy { fill: var(--brand-navy); }
  .company-name {
    font-family: "Crimson Text", serif;
    font-weight: 700;
    font-size: 74px;
    letter-spacing: 1px;
    fill: var(--ink);
  }
  .company-suffix,
  .contact-line,
  .website {
    font-family: "Crimson Text", serif;
    font-weight: 400;
    font-size: 44px;
    fill: var(--ink);
  }
  .slogan {
    font-family: "Shadows Into Light", cursive;
    font-size: 31px;
    fill: var(--card-white);
  }
</style>
</head>
<body>
<svg class="business-card" viewBox="0 0 1050 600" preserveAspectRatio="none" xmlns="http://www.w3.org/2000/svg" role="img" aria-label="OLUNDEX International business card">
  <rect class="card-base" x="0" y="0" width="1050" height="600"/>

  <g class="top-wave">
    <path class="wave-gold" d="M330,0 L1050,0 L1050,98 C850,68 560,30 330,0 Z"/>
    <path class="wave-navy" d="M520,0 L1050,0 L1050,72 C860,42 680,14 520,0 Z"/>
  </g>

  <g class="bottom-wave">
    <path class="wave-gold" d="M0,420 C260,440 520,535 800,530 C900,530 990,528 1050,526 L1050,600 L0,600 Z"/>
    <path class="wave-navy" d="M0,450 C280,470 520,560 820,560 C920,560 1000,558 1050,556 L1050,600 L0,600 Z"/>
  </g>

  <g class="brand-block">
    <text class="company-name" x="40" y="127">OLUNDEX</text>
    <text class="company-suffix" x="39" y="187">International</text>
  </g>

  <g class="contact-block" text-anchor="middle">
    <text class="contact-line" x="525" y="255">John R. Doe</text>
    <text class="contact-line" x="525" y="315">CEO</text>
    <text class="contact-line" x="525" y="374">(555) 123-4567</text>
  </g>

  <text class="website" x="1005" y="508" text-anchor="end">www.yourwebsite.com</text>

  <text class="slogan" x="36" y="565">simple solutions for complex problems</text>
</svg>
</body>
</html>
```